Architecture firm needing a business card

We need a business card design for a new company based in the US called "Dorrance Architecture". Seeking minimalist designs that have a creativity/design feel but must be clean and professional. Please refer to the logo attached.

Target Market(s)

Real Estate Investors, Home Builders and Construction Firms.

Industry/Entity Type

Architecture

Contact Information for Business Card

Standard US size business cards. Would like to have some sort of graphic on the back side of the card - nothing that is too loud but something that may catch your attention. More or less grayscale colors that are in line with the logo colors (navy and greys essentially). Additional colors maybe accepted if blended properly (earthtones), but might be difficult to accomplish and maintain the clean/minimalist look.

Requirements
Must have
• Clean Lines
Nice to have
• some sort of graphics, would like to have something creative on the back side of the card
Should not have
• nothing too busy, cluttered or overwhelming.

```html
<!DOCTYPE html>
<html lang="en">
<head>
<meta charset="utf-8">
<title>Dorrance Architecture – Business Card</title>
<link href="https://fonts.googleapis.com/css2?family=Open+Sans:wght@400;600;700&display=swap" rel="stylesheet">
<style>
  :root {
    --navy: #1d4f7a;
    --navy-deep: #163c5e;
    --grey: #8e9092;
    --card-white: #ffffff;
    --back-top: #d4d5d6;
    --back-bottom: #8d8e90;
    --stage: #e7e8ea;
  }
  * { box-sizing: border-box; margin: 0; padding: 0; }
  html, body { width: 1200px; height: 913px; overflow: hidden; }
  body {
    background: var(--stage);
    font-family: "Open Sans", Arial, sans-serif;
    position: relative;
  }
  .card {
    position: absolute;
    width: 540px;
    height: 309px;
    border-radius: 4px;
    overflow: hidden;
    box-shadow: 0 6px 18px rgba(0,0,0,.18);
  }

  /* Shared wordmark */
  .brand {
    position: absolute;
    display: flex;
    align-items: center;
    gap: 12px;
    color: var(--navy);
    font-weight: 400;
    text-transform: uppercase;
    line-height: 1.05;
    white-space: nowrap;
  }
  .brand-square { width: 34px; height: 34px; background: var(--navy); flex: none; }
  .brand small { display: block; }

  /* Front */
  .card-front { left: 50px; top: 110px; background: var(--card-white); }
  .card-front .brand { left: 38px; top: 50px; font-size: 27px; letter-spacing: 3px; }
  .card-front .brand small { font-size: 13px; letter-spacing: 5px; }

  .holder { position: absolute; right: 38px; top: 48px; text-align: right; }
  .holder-name { color: var(--navy); font-weight: 700; font-size: 19px; letter-spacing: .5px; }
  .holder-role { color: var(--grey); font-size: 10px; letter-spacing: 1px; text-transform: uppercase; }
  .holder-rule {
    position: absolute; left: 38px; right: 20px; top: 124px;
    height: 1.5px; background: var(--navy);
  }
  .edge-tab { position: absolute; right: 0; top: 44px; width: 12px; height: 22px; background: var(--navy); }

  .address {
    position: absolute; left: 38px; top: 148px;
    color: var(--navy-deep); font-weight: 600; font-size: 13px; line-height: 1.35;
  }
  .address-rule { position: absolute; left: 38px; top: 188px; width: 200px; height: 1.5px; background: var(--navy); }
  .contact {
    position: absolute; left: 38px; top: 202px; list-style: none;
    color: var(--navy-deep); font-weight: 600; font-size: 13px; line-height: 1.55;
  }
  .contact li { display: flex; align-items: center; gap: 8px; }
  .contact svg { width: 11px; height: 11px; fill: none; stroke: var(--grey); stroke-width: 1.6; }

  /* Back */
  .card-back {
    left: 610px; top: 490px;
    background: linear-gradient(160deg, var(--back-top) 0%, #b3b4b6 55%, var(--back-bottom) 100%);
    border-right: 6px solid var(--navy);
  }
  .card-back .brand { left: 48px; top: 122px; font-size: 32px; letter-spacing: 4px; gap: 12px; }
  .card-back .brand small { font-size: 14px; letter-spacing: 6px; }
  .card-back .brand-square { width: 40px; height: 40px; }
  .skyline {
    position: absolute; right: 0; top: 56px; width: 130px; height: 96px;
    background: linear-gradient(180deg, rgba(29,79,122,.45), var(--navy));
  }
</style>
</head>
<body>
  <section class="card card-front">
    <div class="brand">
      <span class="brand-square"></span>
      <span>Dorrance<small>Architecture</small></span>
    </div>

    <div class="holder">
      <p class="holder-name">MARCUS HALE</p>
      <p class="holder-role">Owner</p>
    </div>
    <span class="edge-tab"></span>
    <span class="holder-rule"></span>

    <p class="address">1180 Harbor Rd, Alder<br>LA 70512, United States</p>
    <span class="address-rule"></span>

    <ul class="contact">
      <li>
        <svg viewBox="0 0 12 12"><path d="M3 1 L5 3.5 L4 5 Q5.5 7 7 8 L8.5 7 L11 9 L9.5 11 Q5 10.5 1 3 Z"/></svg>
        +1 555-0142
      </li>
      <li>
        <svg viewBox="0 0 12 12"><rect x="1" y="2.5" width="10" height="7"/><path d="M1 2.5 L6 6.5 L11 2.5"/></svg>
        info@marcushale.com
      </li>
      <li>
        <svg viewBox="0 0 12 12"><circle cx="6" cy="6" r="5"/><path d="M1 6 H11 M6 1 Q3 6 6 11 Q9 6 6 1"/></svg>
        www.dorrancearchitecture.com
      </li>
    </ul>
  </section>

  <section class="card card-back">
    <div class="skyline" role="img" aria-label="City skyline silhouette in navy"></div>
    <div class="brand">
      <span class="brand-square"></span>
      <span>Dorrance<small>Architecture</small></span>
    </div>
  </section>
</body>
</html>
```